Dentistry Office

We want a new design for a Dentist's office website.

The theme is: "We provide high quality, state-of-the-art, dental care in a comfortable, caring environment."

The site currently has a menu on the left of the page with about 40 items on it. There is a great deal of textual content on each page, plus several illustrations.

We want to do this using CSS, so we need specifications in the CSS for all possible elements. The CSS needs to be named in a logical manner for easy use.

Every dentist on the planet seems to use lots of Flash. We don't want to because it is so distracting. We are looking for an elegant solution targeting 24-55 age group, but not excluding anyone.

The following (from another dentist's site) can give you a taste of what we want to communicate on the site:

"After 20 years of teaching dentists how to refine their technique and many years of writing textbooks, I currently devote my time to my office and the hands-on practice of dentistry. I'd like to welcome you personally to my dental practice, and I invite you to meet my highly experienced team of professionals.

"We have offered complete dental care of the highest quality since 1978. We provide Preventive Services, Tooth Whitening and Cosmetic Dentistry for a beautiful smile, Endodontics (root canal treatment) to treat painful teeth, Sedation Dentistry so you can relax, and Dental Implants to restore what is missing. We offer total care.

"Our approach to your health is simple: We use our education, experience and dedication to provide every patient with superior dental care.

"This passion for excellence is not just a goal, but a standard every member of our team holds.

"We also pride ourselves with our state of the art procedures, training and technology. This includes creating a beautiful smile using techniques that preserve as much of the original tooth as possible.

"Our abilities are renowned throughout the dental profession and I hope if you have any questions you will contact us by an e-mail note, by phone or just by dropping by."

Keep in mind the screen shape and dimensions. Your design needs to work in the normal screen proportions, regardless of how it looks when you post it here. Scrolling is OK, but the first impression needs to work.

Keep in mind that there will be about 250 words, or more, on each page.

Competitors web sites:

http://www.brevalkoortho.example/

http://www.quimbelfieldcare.example/

http://www.grinsatdoverellclinic.example/

http://www.trunwickfamilydentalcare.example/

http://www.morvanhaledental.example/

http://www.ubrigandental.example/

We need to compete with these.

Target Market(s)

Generally adults seeking the most experienced and comfortable-to-be-with dentist.

Industry/Entity Type

Training

Requirements
Must have
• Must stand apart from other dentists.
• Must be elegant.
• Must have a horizontal menu structure across all columns, NOT a vertical that requires scrolling, no popout, pop down, etc. menus.
• We are looking for something special.
• Do not waste your time or ours putting up templates and things you have used before.
• Personally, I do not see how someone outside the US can understand the northern California dental market. But you are welcome to try.
Should not have
• Flash or graphics that move
• The look of a template
• Folksy fonts
• Looks like you used it 20 times before

```html
<!DOCTYPE html>
<html lang="en">
<head>
<meta charset="utf-8">
<title>Larkmont Dentist – Tobias Wrenfield</title>
<link rel="stylesheet" href="https://fonts.googleapis.com/css2?family=Arimo:wght@400;700&family=Open+Sans:wght@400;600&display=swap">
<style>
:root{
  --teal:#137a68;
  --teal-dark:#0e6b5b;
  --ink:#111;
  --muted:#8c8c8c;
  --rule:#c9c9c9;
  --slate:#6f8089;
  --slate-light:#9eaeb5;
  --nav:#000;
  --page:#fff;
  --backdrop-a:#9d9d9d;
  --backdrop-b:#c2c2c2;
}
*{margin:0;padding:0;box-sizing:border-box}
html,body{width:1043px;height:1200px;overflow:hidden}
body{background:linear-gradient(90deg,var(--backdrop-a),var(--backdrop-b) 50%,var(--backdrop-a));font-family:"Arimo",Arial,sans-serif;color:var(--ink);position:relative}
.page{position:absolute;left:46px;top:0;width:948px;height:1200px;background:var(--page)}
.abs{position:absolute}
.site-title{left:27px;top:2px;font-family:"Open Sans",sans-serif;font-weight:400;font-size:29px;color:var(--teal);letter-spacing:.3px;line-height:34px}
.banner{left:0;top:34px;width:948px;height:207px}
.banner-panel{left:0;top:0;width:568px;height:207px;background:linear-gradient(90deg,var(--slate) 0%,var(--slate-light) 45%,var(--slate) 100%)}
.banner-name{left:25px;top:0;font-family:"Open Sans",sans-serif;font-size:27px;color:#fff;line-height:32px}
.banner-address{left:29px;top:46px;font-weight:700;font-size:14px;color:#fff}
.banner-copy{left:29px;top:76px;width:500px;font-size:12.3px;line-height:16.7px;color:#fff}
.banner-copy p+p{margin-top:16.7px}
.banner-photo{left:568px;top:0;width:380px;height:207px;background:linear-gradient(160deg,#8a8f8c 0%,#6d5a4a 40%,#4f5b3c 75%,#6f7d52 100%)}
.topics{left:0;top:253px;width:948px;height:170px}
.topic{position:absolute;top:0}
.topic h2{font-family:"Open Sans",sans-serif;font-weight:400;font-size:15px;color:var(--teal);line-height:20px;margin-bottom:3px}
.topic li{list-style:none;font-size:11.3px;line-height:14.6px;color:var(--muted)}
.topic-rule{position:absolute;top:0;width:1px;background:var(--rule)}
.main-nav{left:0;top:438px;width:948px;height:28px;background:var(--nav)}
.main-nav a{position:absolute;top:0;line-height:28px;font-weight:700;font-size:11.3px;color:#fff;text-decoration:none}
.sidebar-rule{left:189px;top:466px;width:1px;height:734px;background:var(--rule)}
.offer{left:0;top:466px;width:189px;height:223px;background:var(--slate)}
.offer-title{left:15px;top:54px;width:170px;font-weight:700;font-size:16.5px;line-height:21px;color:#fff}
.offer-note{left:15px;top:160px;width:172px;font-size:10px;line-height:12.5px;color:#000}
.section-divider{left:190px;top:689px;width:758px;border-top:1px dashed var(--slate)}
.section-heading{font-family:"Open Sans",sans-serif;font-weight:400;font-size:14.5px;color:var(--teal);line-height:20px}
.provides{left:214px;top:484px}
.provides-list{left:212px;top:520px;width:720px}
.provides-list li{list-style:none;font-size:12px;line-height:16.7px;padding-left:17px;position:relative}
.provides-list li::before{content:"*";position:absolute;left:0;top:1px;color:var(--teal);font-weight:700;font-size:17px;line-height:17px}
.provides-list b{font-weight:700}
.hours{left:15px;top:714px;width:172px}
.hours .section-heading{margin-bottom:10px}
.hours-lead{font-weight:700;font-size:11px;line-height:16.7px}
.hours li{list-style:none;font-size:11px;line-height:16.7px}
.side-link{left:15px;font-family:"Open Sans",sans-serif;font-size:14.5px;color:var(--teal);text-decoration:none;line-height:20px}
.side-contact{left:15px;top:1050px;width:172px;font-size:12px;line-height:16.7px;color:var(--teal)}
.side-contact strong{font-size:14px}
.side-contact p+p{margin-top:16.7px}
.commitment{left:214px;top:714px;width:730px}
.commitment .section-heading{margin-bottom:13px}
.commitment p{font-size:12px;line-height:16.7px;margin-bottom:16.7px}
.commitment .lead{width:690px}
.commitment .motto{color:var(--teal);font-weight:700;font-style:italic}
</style>
</head>
<body>
<div class="page">
  <div class="abs site-title">LARKMONT DENTIST</div>

  <header class="abs banner">
    <div class="abs banner-panel">
      <div class="abs banner-name">Tobias Wrenfield</div>
      <div class="abs banner-address">Located at 2280 Fennick Avenue, Ste B-3, Larkmont, CA 95999</div>
      <div class="abs banner-copy">
        <p>In Larkmont, when you’re a patient of Dr. Wrenfield, you can be confident that you’re receiving care from the most experienced, knowledgeable, and skilled cosmetic dentist in Calderra County.</p>
        <p>Dr. Wrenfield is an award-winning leader in restorative dentistry and a genial professional. His humor, dedication, and talent ensure you a pleasant experience and superb, long-lasting results.</p>
      </div>
    </div>
    <div class="abs banner-photo" role="img" aria-label="Photograph of the shingled dental office building among garden plants"></div>
  </header>

  <nav class="abs topics">
    <div class="topic" style="left:27px">
      <h2>EDUCATION</h2>
      <ul><li>Emergency Dental Care</li><li>Your Mouth</li><li>Your Tooth</li><li>Cracked Tooth?</li><li>Missing a Tooth?</li><li>Sensitive Teeth</li><li>Dry Mouth</li><li>Tooth Grinding</li><li>Sleep Dentistry</li><li>Videos</li></ul>
    </div>
    <div class="topic-rule" style="left:191px;height:104px"></div>
    <div class="topic" style="left:211px">
      <h2>PREVENTATIVE</h2>
      <ul><li>What is Preventive Care?</li><li>Taking Care of Your Teeth</li><li>Eating Right</li><li>Dental Check-Ups</li><li>Sealants</li><li>Periodontal Disease</li><li>Kicking the Habit</li><li>Night Guards</li><li>Dental X-Rays</li><li>Antibiotics with Treatment</li></ul>
    </div>
    <div class="topic-rule" style="left:377px;height:104px"></div>
    <div class="topic" style="left:396px">
      <h2>COSMETICS</h2>
      <ul><li>Cosmetic Dentistry</li><li>Bleaching and Whitening</li><li>Cosmetic Bonding</li><li>Esthetic Veneers</li><li>Tooth Shaping</li></ul>
    </div>
    <div class="topic-rule" style="left:568px;height:104px"></div>
    <div class="topic" style="left:587px">
      <h2>RESTORATIONS</h2>
      <ul><li>Crowns/Caps: Each Step</li><li>CMBRs</li><li>Porcelain Bridges</li><li>Bonded Dental Bridges</li><li>Gold Restorations</li><li>Implants</li><li>Treating Cracked Teeth</li><li>Periodontal (gum) Treatment</li></ul>
    </div>
    <div class="topic-rule" style="left:760px;height:104px"></div>
    <div class="topic" style="left:777px">
      <h2>VISITING OUR OFFICE</h2>
      <ul><li>Where to Stay</li><li>First Visit / Map</li><li>Financial Policy</li><li>Dental Insurance</li></ul>
    </div>
  </nav>

  <nav class="abs main-nav">
    <a style="left:27px">HOME</a>
    <a style="left:119px">WHY WE ARE DIFFERENT</a>
    <a style="left:308px">TECHNOLOGIES WE OFFER</a>
    <a style="left:510px">MEET DR. WRENFIELD</a>
    <a style="left:668px">OUR STAFF</a>
    <a style="left:786px">CONTACT US / LINKS</a>
  </nav>

  <div class="abs sidebar-rule"></div>

  <aside class="abs offer">
    <div class="abs offer-title">We offer an Initial Patient Examination, X-rays and Cleaning for $79.00.</div>
    <div class="abs offer-note">**New patients only. Offers are<br>&nbsp;&nbsp;&nbsp;cash patients only. Insurance<br>&nbsp;&nbsp;&nbsp;will be billed at full value.</div>
  </aside>

  <h2 class="abs section-heading provides">DR. WRENFIELD PROVIDES</h2>
  <ul class="abs provides-list">
    <li><b>General dentistry</b> - oral hygiene, cavity detection and repair, crowns.</li>
    <li><b>Cosmetic/restorative dentistry</b> - broken or misshapen teeth, crooked smiles, unsightly gaps</li>
    <li><b>Non-metal fillings</b> - nontoxic, durable tooth-colored resin fillings that are proven to provide better results</li>
    <li><b>Tooth shaping</b> - extending, shortening or otherwise reshaping teeth for improved esthetics</li>
    <li><b>Complete smile make-over's</b> - resin veneers that reshape the whole mouth while preserving natural teeth</li>
    <li><b>Tooth whitening</b> - at-home bleaching options to make teeth appear years younger</li>
    <li><b>Laser Dentistry, Sleep Dentistry, and Implant Dentistry with the Finest and Latest Equipment and Materials.</b></li>
    <li><b>Dental Implants to replace missing teeth.</b></li>
    <li><b>Sedation Dentistry so you can be relaxed.</b></li>
  </ul>

  <div class="abs section-divider"></div>

  <section class="abs hours">
    <h2 class="section-heading">OFFICE HOURS</h2>
    <p class="hours-lead">Our usual office hours are:</p>
    <ul><li>Monday 9 am to 6 pm</li><li>Tuesday 9 am to 5 pm</li><li>Wednesday 9 am to 5 pm</li><li>Thursday 9 am to 5 pm</li><li>Friday 7:30 am to 5 pm</li></ul>
  </section>
  <a class="abs side-link" style="top:881px">MAP TO OFFICE</a>
  <a class="abs side-link" style="top:914px">WHERE TO STAY?</a>

  <div class="abs side-contact">
    <p>Please contact us at<br><strong>(555) 014-2290.</strong></p>
    <p>To contact us outside office hours for an emergency, please call <strong>(555) 017-6643.</strong></p>
  </div>

  <section class="abs commitment">
    <h2 class="section-heading">DR. WRENFIELD’S COMMITMENT</h2>
    <p class="lead">After 25 years of teaching dentists how to refine their technique and many years of writing textbooks, I currently devote my time to my office and the hands-on practice of dentistry. I'd like to welcome you personally to my dental practice, and I invite you to meet my highly experienced team of professionals.</p>
    <p>Dr. Wrenfield and his Associated have offered complete dental care of the highest quality since 1978. We provide Preventive Services, Tooth Whitening and Cosmetic Dentistry for a beautiful smile, Endodontics (root canal treatment) to treat painful teeth, Sedation Dentistry so you can relax, and Dental Implants to restore what is missing. We offer total care.</p>
    <p class="motto">Our approach to your health is simple: We use our education, experience and dedication to provide every patient with superior dental care.</p>
    <p class="motto">This passion for excellence is not just a goal, but a standard every member of our team holds.</p>
    <p class="lead">We also pride ourselves with our state of the art procedures, training and technology. This includes creating a beautiful smile using techniques that preserve as much of the original tooth as possible.</p>
    <p class="lead">Our abilities are renowned throughout the dental profession and I hope if you have any questions you will contact us by an e-mail note, by phone or just by dropping by.</p>
    <p>Thank you.</p>
    <p>Sincerely,</p>
    <p>Tobias Wrenfield, DDS FAGD</p>
  </section>
</div>
</body>
</html>
```